Magnetic Business Card Design. One sided

Not happy yet with a design yet currently winning so far are the designs 5162585 5135573 5132280

Logo
unmatched Quality through traditional friendly service" sound like a good line. Blockages, Hot water units & all plumbing services.
7days,
free quote: 0467 215 340
Maybe put on it: Qualified, Licensed
www.brightflowplumbing.com.au

Make word as big so it is clearly able to be read

BrightFlow Plumbing PTY LTD, target market is the middle aged mostly woman professional that owns a house and would rather pay a professional to do the job rather then a handyman.
We are a plumbing company based in Melbourne small and family owned with a focus on service to our customers.

I am after a design that is clean, professional and appealing to the eye which fits with the visual appearance of my web site and logo.

Our most profitable jobs are blockages and hot water units. however we do all types of plumbing. Maybe a point to make on the cards not sure tho.

I have included our previous magnet that i had designed with a pixel press template. if you can improve what we say to get new customers or totally change what is on the magnet. that would be fantastic.

I will also include other marketing material i have previously used

"unmatched Quality Through traditional friendly service" Could be a good catch line

These magnets are dropped into thousands of letter boxes and hopefully will find there way onto new clients fridges. Fridges in million dollar plus houses.

I really look forward to seeing your design. Thank you

Industry/Entity Type

Marketing

Contact Information for Business Card

Number: 0467 215 340
Web site: www.Brightflowplumbing.com.au

```html
<!DOCTYPE html>
<html lang="en">
<head>
<meta charset="utf-8">
<title>BrightFlow Plumbing – Business Card</title>
<link href="https://fonts.googleapis.com/css2?family=Roboto:wght@300;400;500&display=swap" rel="stylesheet">
<style>
  :root {
    --backdrop: #bcc1b9;
    --card: #f2f2f0;
    --teal: #45abc3;
    --ink: #2a2a2a;
    --navy: #2f3b5c;
    --white: #ffffff;
  }
  html, body {
    margin: 0;
    width: 1200px;
    height: 1000px;
    overflow: hidden;
    background: var(--backdrop);
    font-family: "Roboto", Arial, sans-serif;
  }
  .card {
    position: absolute;
    left: 150px;
    top: 220px;
    width: 900px;
    height: 560px;
    background: var(--card);
    box-shadow: 0 6px 18px rgba(0,0,0,0.15);
  }
  .brand-band {
    position: absolute;
    left: 60px;
    top: 50px;
    width: 570px;
    height: 270px;
    background: var(--teal);
    color: var(--white);
  }
  .band-rule {
    position: absolute;
    height: 2px;
    background: var(--white);
    opacity: 0.9;
  }
  .band-rule--top { left: 290px; right: 40px; top: 45px; }
  .band-rule--bottom { left: 90px; right: 40px; top: 225px; }
  .company-name {
    position: absolute;
    left: 45px;
    top: 105px;
    margin: 0;
    font-size: 42px;
    font-weight: 500;
    letter-spacing: 0.5px;
  }
  .tagline {
    position: absolute;
    left: 45px;
    top: 158px;
    margin: 0;
    font-size: 31px;
    font-weight: 300;
    letter-spacing: 0.5px;
  }
  .logo-name {
    position: absolute;
    left: 650px;
    top: 205px;
    display: flex;
    align-items: center;
    gap: 12px;
    font-size: 40px;
    font-weight: 500;
    color: var(--navy);
  }
  .logo-dot {
    width: 18px;
    height: 18px;
    border-radius: 50%;
    background: var(--navy);
  }
  .contact-list {
    position: absolute;
    left: 100px;
    top: 370px;
    margin: 0;
    padding: 0;
    list-style: none;
  }
  .contact-item {
    display: flex;
    align-items: center;
    height: 52px;
  }
  .contact-icon {
    width: 34px;
    height: 34px;
    margin-right: 30px;
    fill: var(--teal);
  }
  .contact-text {
    font-size: 19px;
    color: var(--ink);
    letter-spacing: 0.3px;
  }
</style>
</head>
<body>
  <main class="card">
    <section class="brand-band">
      <div class="band-rule band-rule--top"></div>
      <h1 class="company-name">BRIGHTFLOW PLUMBING</h1>
      <p class="tagline">FAMILY OWNED SINCE 1980</p>
      <div class="band-rule band-rule--bottom"></div>
    </section>

    <div class="logo-name"><span class="logo-dot"></span>BrightFlow</div>

    <ul class="contact-list">
      <li class="contact-item">
        <svg class="contact-icon" viewBox="0 0 34 34" aria-hidden="true">
          <rect x="2" y="7" width="30" height="21"/>
          <polyline points="3,8 17,20 31,8" fill="none" stroke="#f2f2f0" stroke-width="2"/>
        </svg>
        <span class="contact-text">0467 215 340</span>
      </li>
      <li class="contact-item">
        <svg class="contact-icon" viewBox="0 0 34 34" aria-hidden="true">
          <path d="M8 4 L13 4 L15 11 L11 14 C13 19 16 22 21 24 L24 20 L31 22 L31 27 C31 29 29 31 27 31 C15 30 4 19 3 8 C3 6 5 4 8 4 Z"/>
        </svg>
        <span class="contact-text">HELLO@BRIGHTFLOWMAIL.COM.AU</span>
      </li>
      <li class="contact-item">
        <svg class="contact-icon" viewBox="0 0 34 34" aria-hidden="true">
          <circle cx="17" cy="17" r="15"/>
          <g fill="none" stroke="#f2f2f0" stroke-width="1.6">
            <ellipse cx="17" cy="17" rx="6" ry="15"/>
            <line x1="2" y1="17" x2="32" y2="17"/>
            <line x1="5" y1="10" x2="29" y2="10"/>
            <line x1="5" y1="24" x2="29" y2="24"/>
          </g>
        </svg>
        <span class="contact-text">WWW.BRIGHTFLOWPLUMBING.COM.AU</span>
      </li>
    </ul>
  </main>
</body>
</html>
```